300 x 250 Web Ad for Porn Website

300 x 250 web ad that will appear on a porn site. Need to see 3 options, one with each of the 3 girls. Remove the background around the girls.

Underneath the girls image should read in big bold letters: High Speed Internet
Underneath in slightly smaller size: NO Credit Check

To the left of the girl: Save MONEY...

To the right of the girl: So you can buy more PORN

We want it to look very unique, raunchy, and eye catching.

Target Market(s)

Porn website

Industry/Entity Type

Internet Service Provider

Colors

Designer to choose colors to be used in the design.

Requirements
Must have
• Must stand out so people will definitely notice it.
• JPEG and PNG formats

```html
<!DOCTYPE html>
<html lang="en">
<head>
<meta charset="UTF-8">
<title>High Speed Internet Ad Options</title>
<link rel="stylesheet" href="https://fonts.googleapis.com/css2?family=Oswald:wght@500;600&family=Montserrat:wght@700&display=swap">
<style>
  :root {
    --page-bg: #efefef;
    --ad-bg-top: #262626;
    --ad-bg-bottom: #0e0e0e;
    --purple-top: #b21ed8;
    --purple-bottom: #8a12c4;
    --green-top: #10b848;
    --green-bottom: #079236;
    --orange-top: #ff7a10;
    --orange-bottom: #ff3a00;
    --white: #ffffff;
    --needle-red: #f23a0c;
    --model-light: #c9977a;
    --model-dark: #6e4a3a;
  }
  html, body {
    margin: 0;
    padding: 0;
    width: 1200px;
    height: 2182px;
    overflow: hidden;
    background: var(--page-bg);
  }
  .ad-option {
    position: absolute;
    left: 273px;
    width: 655px;
    height: 545px;
    display: block;
  }
  .ad-option--one { top: 131px; }
  .ad-option--two { top: 803px; }
  .ad-option--three { top: 1512px; }
  .circle-label {
    font-family: 'Oswald', sans-serif;
    font-weight: 500;
    fill: var(--white);
    text-anchor: middle;
  }
  .save-label { font-size: 25px; }
  .porn-label { font-size: 19.5px; }
  .headline {
    font-family: 'Oswald', sans-serif;
    font-weight: 600;
    font-size: 19px;
    fill: var(--white);
  }
  .subline {
    font-family: 'Montserrat', sans-serif;
    font-weight: 700;
    font-size: 12.5px;
    fill: var(--white);
  }
</style>
</head>
<body>

<svg width="0" height="0" style="position:absolute">
  <defs>
    <linearGradient id="adBackground" x1="0" y1="0" x2="0" y2="1">
      <stop offset="0" stop-color="var(--ad-bg-top)"/>
      <stop offset="1" stop-color="var(--ad-bg-bottom)"/>
    </linearGradient>
    <linearGradient id="purpleFill" x1="0" y1="0" x2="0" y2="1">
      <stop offset="0" stop-color="var(--purple-top)"/>
      <stop offset="1" stop-color="var(--purple-bottom)"/>
    </linearGradient>
    <linearGradient id="greenFill" x1="0" y1="0" x2="0" y2="1">
      <stop offset="0" stop-color="var(--green-top)"/>
      <stop offset="1" stop-color="var(--green-bottom)"/>
    </linearGradient>
    <linearGradient id="orangeFill" x1="0" y1="0" x2="0" y2="1">
      <stop offset="0" stop-color="var(--orange-top)"/>
      <stop offset="1" stop-color="var(--orange-bottom)"/>
    </linearGradient>
    <linearGradient id="modelFill" x1="0" y1="0" x2="0" y2="1">
      <stop offset="0" stop-color="var(--model-dark)"/>
      <stop offset="0.5" stop-color="var(--model-light)"/>
      <stop offset="1" stop-color="var(--model-dark)"/>
    </linearGradient>
    <clipPath id="adClip"><rect width="300" height="250"/></clipPath>
    <g id="speedGauge">
      <path d="M27 248 A31 31 0 1 1 89 248 Z" fill="var(--white)"/>
      <g stroke="var(--needle-red)" stroke-width="2.4" stroke-linecap="round">
        <line x1="36" y1="238" x2="40" y2="236"/>
        <line x1="40" y1="225" x2="43.5" y2="227.5"/>
        <line x1="49" y1="217" x2="51" y2="221"/>
        <line x1="58" y1="214" x2="58" y2="218.5"/>
        <line x1="67" y1="217" x2="65" y2="221"/>
        <line x1="76" y1="225" x2="72.5" y2="227.5"/>
        <line x1="80" y1="238" x2="76" y2="236"/>
      </g>
      <line x1="58" y1="241" x2="67" y2="223" stroke="var(--needle-red)" stroke-width="3.2" stroke-linecap="round"/>
      <circle cx="58" cy="241" r="4.2" fill="var(--needle-red)"/>
    </g>
    <g id="adFrame">
      <rect width="300" height="250" fill="url(#adBackground)"/>
      <circle cx="53" cy="105" r="65" fill="url(#purpleFill)"/>
      <circle cx="237" cy="67" r="68" fill="url(#greenFill)"/>
      <text class="circle-label save-label" x="53" y="101">SAVE</text>
      <text class="circle-label save-label" x="53" y="126">MONEY</text>
      <text class="circle-label porn-label" x="249" y="31">SO YOU</text>
      <text class="circle-label porn-label" x="249" y="51">CAN</text>
      <text class="circle-label porn-label" x="249" y="71">BUY MORE</text>
      <text class="circle-label porn-label" x="249" y="91">PORN</text>
    </g>
    <g id="adFooter">
      <path d="M0 206 Q150 186 300 206 L300 250 L0 250 Z" fill="url(#orangeFill)"/>
      <use href="#speedGauge"/>
      <text class="headline" x="101" y="225">HIGH SPEED INTERNET</text>
      <text class="subline" x="101" y="242">NO CREDIT CHECK</text>
    </g>
  </defs>
</svg>

<svg class="ad-option ad-option--one" viewBox="0 0 300 250">
  <g clip-path="url(#adClip)">
    <use href="#adFrame"/>
    <rect class="model-photo" x="96" y="4" width="110" height="200" rx="40" fill="url(#modelFill)" role="img" aria-label="Cut-out photo of a model in red lingerie and an open jacket"/>
    <use href="#adFooter"/>
  </g>
</svg>

<svg class="ad-option ad-option--two" viewBox="0 0 300 250">
  <g clip-path="url(#adClip)">
    <use href="#adFrame"/>
    <rect class="model-photo" x="106" y="4" width="100" height="200" rx="40" fill="url(#modelFill)" role="img" aria-label="Cut-out photo of a model in black lingerie seen from behind"/>
    <use href="#adFooter"/>
  </g>
</svg>

<svg class="ad-option ad-option--three" viewBox="0 0 300 250">
  <g clip-path="url(#adClip)">
    <use href="#adFrame"/>
    <rect class="model-photo" x="112" y="10" width="84" height="194" rx="36" fill="url(#modelFill)" role="img" aria-label="Cut-out photo of a model in a sheer nude bodysuit"/>
    <use href="#adFooter"/>
  </g>
</svg>

</body>
</html>
```